Technical Refinement & Corporate Adaptation of AI Graphics

We have a follow-up project for you that involves technically refining existing, AI-generated graphics and recreating them professionally in Microsoft PowerPoint. - as you did already. The content and core structure should remain unchanged, but the visual style needs to be aligned with the corporate design of the Wärmewerk Kessing (colors, typography, and visual language). The primary focus is to ensure all elements are fully editable, perfectly aligned, and deliver a clean, scientific-technical look.

```html
<!DOCTYPE html>
<html lang="en">
<head>
<meta charset="utf-8">
<title>Integrated Assessment Slides – Wärmewerk Kessing</title>
<link href="https://fonts.googleapis.com/css2?family=Source+Sans+3:wght@400;600;700&display=swap" rel="stylesheet">
<style>
:root{
  --page:#dcdcdc;
  --card:#ffffff;
  --green-dark:#1a6b4a;
  --green:#5ea83b;
  --green-light:#6ab04c;
  --teal:#157f86;
  --orange:#f29b1c;
  --grey:#8a8d90;
  --grey-light:#b5b7b9;
  --tint:#e8f1ec;
  --bar-bg:#f2f2f2;
  --ink:#222;
  --muted:#555;
}
*{margin:0;padding:0;box-sizing:border-box}
html,body{width:847px;height:1200px;overflow:hidden;background:var(--page)}
body{position:relative;font-family:"Source Sans 3",Arial,sans-serif}
.slide{position:absolute;width:384px;height:216px;background:var(--card);box-shadow:0 1px 3px rgba(0,0,0,.25)}
.slide svg{width:384px;height:216px;display:block}
.col-l{left:31px}.col-r{left:432px}
.row1{top:32px}.row2{top:263px}.row3{top:494px}.row4{top:725px}.row5{top:955px}
svg text{font-family:"Source Sans 3",Arial,sans-serif;fill:var(--ink)}
.num{fill:#fff;font-weight:700;font-size:17px}
.ttl{font-weight:700;font-size:18.5px}
.sub{font-size:12.5px}
.h{font-weight:700;font-size:11px;fill:var(--green-dark)}
.hn{font-weight:400;font-size:11px}
.lbl{font-size:10.5px}
.sm{font-size:9px}
.xs{font-size:8px;fill:var(--muted)}
.val{font-size:9.5px;font-weight:700}
.item{font-size:12.5px;font-weight:600}
.kf-h{font-weight:700;font-size:11.5px;fill:var(--green-dark)}
.kf-t{font-size:11.5px}
.axis{stroke:#bbb;stroke-width:1;fill:none}
.grid{stroke:#ddd;stroke-width:1;fill:none}
.sel{fill:none;stroke:#777;stroke-width:1}
.hdl{fill:#fff;stroke:#666;stroke-width:1}
.wht{fill:#fff}
</style>
</head>
<body>

<!-- 01 Integrated process assessment -->
<section class="slide col-l row1">
<svg viewBox="0 0 735 413" role="group" aria-label="Integrated process assessment">
<symbol id="assessment" viewBox="0 0 735 413">
  <rect x="37" y="24" width="32" height="30" fill="var(--green-dark)"/>
  <text class="num" x="43" y="46">01</text>
  <text class="ttl" x="77" y="33">INTEGRATED PROCESS ASSESSMENT</text>
  <text class="sub" x="77" y="50">for Technology and Product Innovation</text>
  <line x1="37" y1="58" x2="698" y2="58" stroke="var(--green-dark)" stroke-width="1.5"/>
  <g>
    <rect x="88" y="82" width="164" height="46" fill="var(--bar-bg)"/><rect x="36" y="82" width="52" height="46" fill="var(--green-light)"/>
    <path d="M50 117c2-14 12-24 28-26c0 16-10 26-24 26zM52 116l16-16" fill="#fff" stroke="var(--green-light)" stroke-width="1.5"/>
    <text class="item" x="103" y="110">Environmental(LCA)</text>
    <rect x="88" y="143" width="164" height="46" fill="var(--bar-bg)"/><rect x="36" y="143" width="52" height="46" fill="var(--green-light)"/>
    <text x="51" y="180" font-size="34" font-weight="700" style="fill:#fff">$</text>
    <text class="item" x="103" y="171">Economic(TEA)</text>
    <rect x="88" y="204" width="164" height="46" fill="var(--bar-bg)"/><rect x="36" y="204" width="52" height="46" fill="var(--green-light)"/>
    <g fill="#fff"><circle cx="62" cy="218" r="6"/><path d="M51 240c0-9 5-13 11-13s11 4 11 13z"/><circle cx="49" cy="222" r="4"/><circle cx="75" cy="222" r="4"/><path d="M42 238c0-6 3-9 7-9s6 2 6 6zM82 238c0-6-3-9-7-9s-6 2-6 6z"/></g>
    <text class="item" x="103" y="232">Social(S-LCA)</text>
    <rect x="88" y="265" width="164" height="46" fill="var(--bar-bg)"/><rect x="36" y="265" width="52" height="46" fill="var(--green-light)"/>
    <circle cx="62" cy="288" r="13" fill="none" stroke="#fff" stroke-width="6" stroke-dasharray="4 3"/><circle cx="62" cy="288" r="9" fill="#fff"/><circle cx="62" cy="288" r="4" fill="var(--green-light)"/>
    <text class="item" x="103" y="293">Technical(Performance)</text>
  </g>
  <text class="h" x="319" y="89">GENERATION MIX (2035) <tspan class="hn">(normalized)</tspan></text>
  <polygon class="grid" points="424,122 507.7,182.8 475.7,281.2 372.3,281.2 340.3,182.8"/>
  <polygon class="grid" points="424,144 486.8,189.6 462.8,263.4 385.2,263.4 361.2,189.6"/>
  <polygon class="grid" points="424,166 465.8,196.4 449.9,245.6 398.1,245.6 382.2,196.4"/>
  <polygon class="grid" points="424,188 444.9,203.2 436.9,227.8 411.1,227.8 403.1,203.2"/>
  <path class="grid" d="M424 210L424 122M424 210L507.7 182.8M424 210L475.7 281.2M424 210L372.3 281.2M424 210L340.3 182.8"/>
  <g class="xs" text-anchor="end"><text x="419" y="125">1.00</text><text x="419" y="147">0.75</text><text x="419" y="169">0.50</text><text x="419" y="191">0.25</text><text x="419" y="213">0</text></g>
  <polygon points="424,138 486.8,189.6 460.5,260.2 392.8,252.9 369.8,192.4" fill="none" stroke="var(--green)" stroke-width="2"/>
  <polygon points="424,135 492.5,187.8 466.3,268.2 385.2,263.4 373.6,193.6" fill="none" stroke="var(--teal)" stroke-width="2"/>
  <polygon points="424,148 465.8,196.4 449.9,245.6 398.1,245.6 386,197.6" fill="none" stroke="var(--orange)" stroke-width="2"/>
  <g fill="var(--teal)"><circle cx="424" cy="135" r="3"/><circle cx="492.5" cy="187.8" r="3"/><circle cx="466.3" cy="268.2" r="3"/><circle cx="385.2" cy="263.4" r="3"/><circle cx="373.6" cy="193.6" r="3"/></g>
  <g fill="var(--green)"><circle cx="424" cy="138" r="3"/><circle cx="486.8" cy="189.6" r="3"/><circle cx="460.5" cy="260.2" r="3"/><circle cx="392.8" cy="252.9" r="3"/><circle cx="369.8" cy="192.4" r="3"/></g>
  <g class="sm" font-weight="700">
    <text x="424" y="114" text-anchor="middle">Safety</text>
    <text x="512" y="193">Costs</text>
    <text x="515" y="302" text-anchor="middle">Resource Use</text>
    <text x="360" y="297" text-anchor="middle">Technology</text><text x="360" y="309" text-anchor="middle">Performance</text>
    <text x="345" y="185" text-anchor="end">Social</text><text x="345" y="197" text-anchor="end">Acceptance</text>
  </g>
  <g class="lbl" font-weight="600">
    <line x1="550" y1="112" x2="566" y2="112" stroke="var(--green)" stroke-width="2"/><text x="574" y="116">Option A</text>
    <line x1="550" y1="141" x2="566" y2="141" stroke="var(--teal)" stroke-width="2"/><text x="574" y="145">Option B</text>
    <line x1="550" y1="170" x2="566" y2="170" stroke="var(--orange)" stroke-width="2"/><text x="574" y="174">Option C</text>
  </g>
  <rect x="550" y="225" width="148" height="87" rx="4" fill="var(--green-dark)"/>
  <circle cx="577" cy="225" r="14" fill="var(--green-light)" stroke="#fff" stroke-width="2"/>
  <path d="M570 225l5 5l9-9" fill="none" stroke="#fff" stroke-width="2.5"/>
  <g class="sm"><text class="wht" x="564" y="258">Integrated assessment</text><text class="wht" x="564" y="270">enables robust decision-</text><text class="wht" x="564" y="282">making and identifies</text><text class="wht" x="564" y="294">trade-offs.</text></g>
  <rect x="40" y="336" width="658" height="56" rx="5" fill="var(--tint)"/>
  <rect x="40" y="336" width="55" height="56" rx="5" fill="var(--green-dark)"/>
  <g fill="#fff"><circle cx="57" cy="356" r="6"/><circle cx="78" cy="356" r="6"/><path d="M50 366h35v3H50zM66 369l-8 12h18z"/></g>
  <text class="kf-h" x="106" y="358">KEY FINDING</text>
  <text class="kf-t" x="106" y="377">Option B shows the best overall balance across all dimensions.</text>
</symbol>
<use href="#assessment" x="0" y="0" width="735" height="413"/>
</svg>
</section>

<!-- 01 editable layout view -->
<section class="slide col-r row1">
<svg viewBox="0 0 735 413" role="group" aria-label="Editable layout view with selected objects">
  <use href="#assessment" x="0" y="0" width="735" height="413"/>
  <g>
    <rect class="sel" x="75" y="14" width="645" height="42"/>
    <rect class="sel" x="36" y="80" width="216" height="50"/><rect class="sel" x="36" y="141" width="216" height="50"/>
    <rect class="sel" x="36" y="202" width="216" height="50"/><rect class="sel" x="36" y="263" width="216" height="50"/>
    <rect class="sel" x="318" y="78" width="200" height="16"/>
    <rect class="sel" x="340" y="114" width="170" height="172"/>
    <rect class="sel" x="548" y="104" width="96" height="76"/>
    <rect class="sel" x="550" y="210" width="148" height="104"/>
    <rect class="sel" x="40" y="334" width="658" height="60"/>
    <line x1="0" y1="187" x2="735" y2="187" stroke="#999" stroke-dasharray="3 3"/>
    <line x1="424" y1="60" x2="424" y2="413" stroke="#999" stroke-dasharray="3 3"/>
  </g>
  <g>
    <circle class="hdl" cx="75" cy="14" r="3"/><circle class="hdl" cx="720" cy="14" r="3"/><circle class="hdl" cx="75" cy="56" r="3"/><circle class="hdl" cx="720" cy="56" r="3"/>
    <circle class="hdl" cx="36" cy="80" r="3"/><circle class="hdl" cx="252" cy="80" r="3"/><circle class="hdl" cx="252" cy="313" r="3"/><circle class="hdl" cx="36" cy="313" r="3"/>
    <circle class="hdl" cx="340" cy="114" r="3"/><circle class="hdl" cx="510" cy="114" r="3"/><circle class="hdl" cx="340" cy="286" r="3"/><circle class="hdl" cx="510" cy="286" r="3"/>
    <circle class="hdl" cx="550" cy="210" r="3"/><circle class="hdl" cx="698" cy="210" r="3"/><circle class="hdl" cx="550" cy="314" r="3"/><circle class="hdl" cx="698" cy="314" r="3"/>
    <circle class="hdl" cx="40" cy="334" r="3"/><circle class="hdl" cx="698" cy="334" r="3"/><circle class="hdl" cx="40" cy="394" r="3"/><circle class="hdl" cx="698" cy="394" r="3"/>
    <circle class="hdl" cx="548" cy="104" r="3"/><circle class="hdl" cx="644" cy="104" r="3"/><circle class="hdl" cx="548" cy="180" r="3"/><circle class="hdl" cx="644" cy="180" r="3"/>
  </g>
</svg>
</section>

<!-- 02 Socio-economic -->
<section class="slide col-l row2">
<svg viewBox="0 0 735 413" role="group" aria-label="Socio-economic and sociotechnical analyses">
  <rect x="37" y="17" width="32" height="30" fill="var(--green-dark)"/><text class="num" x="43" y="39">02</text>
  <text class="ttl" x="77" y="39">SOCIO-ECONOMIC &amp; SOCIOTECHNICAL ANALYSES</text>
  <line x1="37" y1="58" x2="698" y2="58" stroke="var(--green-dark)" stroke-width="1.5"/>
  <text class="h" x="39" y="97">Stakeholder Acceptance (%) <tspan class="hn">(n = 1,203)</tspan></text>
  <g class="sm" text-anchor="middle"><text x="130" y="127">0</text><text x="171" y="127">20</text><text x="211" y="127">40</text><text x="252" y="127">60</text><text x="292" y="127">80</text><text x="333" y="127">100</text></g>
  <line class="axis" x1="130" y1="135" x2="130" y2="320"/>
  <g fill="var(--green)">
    <rect x="130" y="147" width="164" height="22"/><rect x="130" y="183" width="136" height="22"/><rect x="130" y="219" width="110" height="22"/><rect x="130" y="255" width="99" height="22"/><rect x="130" y="291" width="85" height="22"/>
  </g>
  <g class="sm" text-anchor="end"><text x="122" y="161">Industry</text><text x="122" y="197">Policy Makers</text><text x="122" y="233">Consumers</text><text x="122" y="269">NGOs</text><text x="122" y="305">Local Community</text></g>
  <g class="val"><text x="298" y="162">81</text><text x="270" y="198">67</text><text x="244" y="234">54</text><text x="233" y="270">49</text><text x="219" y="306">42</text></g>
  <line x1="367" y1="85" x2="367" y2="325" stroke="#ddd"/>
  <text class="h" x="393" y="97">Perceived Impact <tspan class="hn">(mean score 1–5)</tspan></text>
  <g class="grid"><line x1="537" y1="110" x2="537" y2="300"/><line x1="588" y1="110" x2="588" y2="300"/><line x1="640" y1="110" x2="640" y2="300"/><line x1="692" y1="110" x2="692" y2="300"/></g>
  <line class="axis" x1="485" y1="110" x2="485" y2="300"/><line class="axis" x1="485" y1="300" x2="692" y2="300"/>
  <g class="sm" text-anchor="middle"><text x="485" y="315">1</text><text x="537" y="315">2</text><text x="588" y="315">3</text><text x="640" y="315">4</text><text x="692" y="315">5</text></g>
  <g stroke="var(--teal)" stroke-width="1.2" fill="none">
    <path d="M519 125H656M519 120v10M656 120v10"/><path d="M539 165H650M539 160v10M650 160v10"/>
    <path d="M524 205H633M524 200v10M633 200v10"/><path d="M514 245H607M514 240v10M607 240v10"/>
    <path d="M498 285H614M498 280v10M614 280v10"/>
  </g>
  <g fill="var(--teal)"><circle cx="604" cy="125" r="4"/><circle cx="594" cy="165" r="4"/><circle cx="570" cy="205" r="4"/><circle cx="560" cy="245" r="4"/><circle cx="568" cy="285" r="4"/></g>
  <g class="sm" text-anchor="end">
    <text x="470" y="121">Economic</text><text x="470" y="133">Benefits</text>
    <text x="470" y="161">Employment</text><text x="470" y="173">Effects</text>
    <text x="470" y="201">Environmental</text><text x="470" y="213">Benefits</text>
    <text x="470" y="241">Technology</text><text x="470" y="253">Risk</text>
    <text x="470" y="281">Social</text><text x="470" y="293">Acceptance</text>
  </g>
  <rect x="40" y="336" width="658" height="56" rx="5" fill="var(--tint)"/><rect x="40" y="336" width="55" height="56" rx="5" fill="var(--green-dark)"/>
  <g fill="#fff"><circle cx="67" cy="354" r="6"/><path d="M56 377c0-9 5-14 11-14s11 5 11 14z"/><circle cx="54" cy="358" r="4"/><circle cx="80" cy="358" r="4"/><path d="M47 374c0-6 3-9 7-9s6 2 6 5zM87 374c0-6-3-9-7-9s-6 2-6 5z"/></g>
  <text class="kf-h" x="106" y="352">KEY FINDING</text>
  <text class="kf-t" x="106" y="369">Economic benefits and employment effects are perceived positively, while technology risk and social</text>
  <text class="kf-t" x="106" y="383">acceptance are critical levers.</text>
</svg>
</section>

<!-- 03 Techno-economic -->
<section class="slide col-r row2">
<svg viewBox="0 0 735 413" role="group" aria-label="Techno-economic analyses">
  <rect x="37" y="17" width="32" height="30" fill="var(--green-dark)"/><text class="num" x="43" y="39">03</text>
  <text class="ttl" x="77" y="39">TECHNO-ECONOMIC ANALYSES</text>
  <line x1="37" y1="58" x2="698" y2="58" stroke="var(--green-dark)" stroke-width="1.5"/>
  <text class="h" x="37" y="86">Stakeholder Acceptance (%) <tspan class="hn">(n = 1,203)</tspan></text>
  <g class="sm" text-anchor="end"><text x="55" y="106">120</text><text x="55" y="135">100</text><text x="55" y="164">80</text><text x="55" y="194">60</text><text x="55" y="223">40</text><text x="55" y="252">20</text><text x="55" y="282">0</text></g>
  <line class="axis" x1="62" y1="102" x2="62" y2="278"/><line class="axis" x1="62" y1="278" x2="270" y2="278"/>
  <g>
    <rect x="78" y="234" width="44" height="44" fill="var(--green)"/><rect x="78" y="190" width="44" height="44" fill="var(--grey-light)"/><rect x="78" y="143" width="44" height="47" fill="var(--teal)"/><rect x="78" y="120" width="44" height="23" fill="var(--orange)"/>
    <rect x="149" y="240" width="44" height="38" fill="var(--green)"/><rect x="149" y="206" width="44" height="34" fill="var(--grey-light)"/><rect x="149" y="165" width="44" height="41" fill="var(--teal)"/><rect x="149" y="139" width="44" height="26" fill="var(--orange)"/>
    <rect x="219" y="257" width="44" height="21" fill="var(--green)"/><rect x="219" y="246" width="44" height="11" fill="var(--teal)"/>
  </g>
  <g class="sm" text-anchor="middle"><text x="100" y="294">S1</text><text x="100" y="306">(Reference)</text><text x="171" y="294">S2</text><text x="171" y="306">(Improvement)</text><text x="241" y="294">S3</text><text x="241" y="306">(Innovative)</text></g>
  <g class="sm">
    <rect x="286" y="102" width="10" height="10" fill="var(--green)"/><text x="302" y="111">CAPEX</text>
    <rect x="286" y="131" width="10" height="10" fill="var(--teal)"/><text x="302" y="140">OPEX</text>
    <rect x="286" y="160" width="10" height="10" fill="var(--grey-light)"/><text x="302" y="169">Fuel</text>
    <rect x="286" y="189" width="10" height="10" fill="var(--orange)"/><text x="302" y="198">CO₂ Price</text>
  </g>
  <line x1="367" y1="80" x2="367" y2="325" stroke="#ddd"/>
  <text class="h" x="383" y="86">Stakeholder Acceptance (%) <tspan class="hn">(n = 1,203)</tspan></text>
  <line class="axis" x1="582" y1="95" x2="582" y2="290"/><line class="axis" x1="480" y1="290" x2="684" y2="290"/>
  <g class="sm" text-anchor="middle"><text x="480" y="308">-30</text><text x="514" y="308">-20</text><text x="548" y="308">-10</text><text x="582" y="308">0</text><text x="616" y="308">10</text><text x="650" y="308">20</text><text x="684" y="308">30</text></g>
  <g>
    <rect x="525" y="103" width="57" height="18" fill="var(--green-light)"/><rect x="582" y="103" width="57" height="18" fill="var(--teal)"/>
    <rect x="534" y="141" width="48" height="18" fill="var(--green-light)"/><rect x="582" y="141" width="48" height="18" fill="var(--teal)"/>
    <rect x="549" y="178" width="33" height="18" fill="var(--green-light)"/><rect x="582" y="178" width="33" height="18" fill="var(--teal)"/>
    <rect x="561" y="215" width="21" height="18" fill="var(--green-light)"/><rect x="582" y="215" width="21" height="18" fill="var(--teal)"/>
    <rect x="570" y="253" width="12" height="18" fill="var(--green-light)"/><rect x="582" y="253" width="12" height="18" fill="var(--teal)"/>
  </g>
  <g class="val"><text x="647" y="116">±16.7</text><text x="638" y="154">±14.2</text><text x="623" y="191">±9.8</text><text x="611" y="228">±6.3</text><text x="602" y="266">±3.6</text></g>
  <g class="sm" text-anchor="end">
    <text x="500" y="109">Capital Cost</text><text x="500" y="121">±20%</text>
    <text x="500" y="147">Electricity Price</text><text x="500" y="159">±30%</text>
    <text x="500" y="184">Capacity Factor</text><text x="500" y="196">±15% (abs)</text>
    <text x="500" y="221">CO₂ Price</text><text x="500" y="233">±50%</text>
    <text x="500" y="259">O&amp;M Cost</text><text x="500" y="271">±20%</text>
  </g>
  <rect x="40" y="336" width="658" height="56" rx="5" fill="var(--tint)"/><rect x="40" y="336" width="55" height="56" rx="5" fill="var(--green-dark)"/>
  <text x="52" y="378" font-size="32" font-weight="700" style="fill:#fff">€</text>
  <text class="kf-h" x="106" y="352">KEY FINDING</text>
  <text class="kf-t" x="106" y="369">Total cost is most sensitive to capital cost and energy price. Technology improvements and renewable</text>
  <text class="kf-t" x="106" y="383">inputs reduce costs significantly.</text>
</svg>
</section>

<!-- 04 Conceptual pre-engineering -->
<section class="slide col-l row3">
<svg viewBox="0 0 735 413" role="group" aria-label="Conceptual pre-engineering">
  <rect x="37" y="17" width="32" height="30" fill="var(--green-dark)"/><text class="num" x="43" y="39">04</text>
  <text class="ttl" x="77" y="39">CONCEPTUAL PRE-ENGINEERING</text>
  <line x1="37" y1="58" x2="698" y2="58" stroke="var(--green-dark)" stroke-width="1.5"/>
  <text class="h" x="41" y="106" font-size="12.5">Process Flow Diagram <tspan font-weight="700" font-size="12.5" style="fill:var(--ink)">(Example)</tspan></text>
  <text class="lbl" x="45" y="134" font-weight="700">Feedstock</text>
  <text class="lbl" x="317" y="134" font-weight="700">Product</text>
  <g stroke="var(--green)" stroke-width="2" fill="none">
    <path d="M53 150H95"/><path d="M160 150H202"/><path d="M285 150H327"/>
    <path d="M300 150V236H78V162"/>
  </g>
  <g fill="var(--green)"><path d="M95 144l10 6l-10 6z"/><path d="M202 144l10 6l-10 6z"/><path d="M327 144l10 6l-10 6z"/><path d="M72 162l6-10l6 10z"/></g>
  <path d="M114 136c0-5 34-5 34 0v32c0 5-34 5-34 0z" fill="#fff" stroke="#222" stroke-width="1.5"/><ellipse cx="131" cy="136" rx="17" ry="4" fill="#fff" stroke="#222" stroke-width="1.5"/>
  <rect x="220" y="130" width="50" height="40" fill="#fff" stroke="#222" stroke-width="1.5"/>
  <circle cx="237" cy="150" r="8" fill="none" stroke="#222" stroke-width="1.5"/><circle cx="253" cy="150" r="8" fill="none" stroke="#222" stroke-width="1.5"/>
  <text class="lbl" x="189" y="224" font-weight="700" text-anchor="middle" style="fill:var(--green)">Recycle</text>
  <path d="M97 269H125" stroke="var(--green)" stroke-width="1.5" stroke-dasharray="4 3"/><path d="M125 265l7 4l-7 4z" fill="var(--green)"/><text class="sm" x="136" y="272">Target</text>
  <path d="M203 269H233" stroke="var(--green-dark)" stroke-width="1.5"/><path d="M233 265l7 4l-7 4z" fill="var(--green-dark)"/><text class="sm" x="246" y="272">Concept</text>
  <text class="h" x="390" y="106" font-size="12.5">Mass &amp; Energy Balance <tspan class="xs" font-weight="400">(per unit output)</tspan></text>
  <g>
    <rect x="390" y="124" width="300" height="25" fill="#f2f2f2"/><rect x="390" y="177" width="300" height="25" fill="#f2f2f2"/><rect x="390" y="230" width="300" height="25" fill="#f2f2f2"/>
    <line x1="588" y1="124" x2="588" y2="255" stroke="#fff" stroke-width="2"/>
  </g>
  <g class="lbl"><text x="399" y="141">Feedstock</text><text x="399" y="168">Utilities</text><text x="399" y="194">Products</text><text x="399" y="221">By-products</text><text x="399" y="247">Emissions (kg CO₂-eq)</text></g>
  <g class="val" text-anchor="end"><text x="680" y="141">1,000</text><text x="680" y="168">850</text><text x="680" y="194">650</text><text x="680" y="221">180</text><text x="680" y="247">42</text></g>
  <rect x="40" y="336" width="658" height="56" rx="5" fill="var(--tint)"/><rect x="40" y="336" width="55" height="56" rx="5" fill="var(--green-dark)"/>
  <circle cx="67" cy="364" r="13" fill="none" stroke="#fff" stroke-width="6" stroke-dasharray="4 3"/><circle cx="67" cy="364" r="9" fill="#fff"/><circle cx="67" cy="364" r="4" fill="var(--green-dark)"/>
  <text class="kf-h" x="106" y="358">KEY FINDING</text>
  <text class="kf-t" x="106" y="377">Concept meets all key targets except CO₂ emissions, where further optimization is needed.</text>
</svg>
</section>

<!-- 05 MCDA -->
<section class="slide col-r row3">
<svg viewBox="0 0 735 413" role="group" aria-label="Multi-criteria decision analysis">
  <rect x="37" y="17" width="32" height="30" fill="var(--green-dark)"/><text class="num" x="43" y="39">05</text>
  <text class="ttl" x="77" y="39">MULTI-CRITERIA DECISION ANALYSIS (MCDA)</text>
  <line x1="37" y1="58" x2="698" y2="58" stroke="var(--green-dark)" stroke-width="1.5"/>
  <text class="h" x="39" y="86">Criteria weights <tspan font-weight="700" style="fill:var(--ink)">(Σ = 1.00)</tspan></text>
  <rect x="39" y="97" width="230" height="24" fill="var(--green-dark)"/>
  <text class="lbl" x="48" y="113" font-weight="700" style="fill:#fff">Criteria</text><text class="lbl" x="260" y="113" font-weight="700" text-anchor="end" style="fill:#fff">Weight</text>
  <g fill="none" stroke="#ccc"><rect x="39" y="121" width="230" height="122"/><path d="M39 145H269M39 170H269M39 194H269M39 218H269M200 121V243"/></g>
  <g class="lbl"><text x="48" y="137">Economic</text><text x="48" y="162">Environmental</text><text x="48" y="186">Technical</text><text x="48" y="211">Social</text><text x="48" y="235">Risk</text></g>
  <g class="val" text-anchor="end"><text x="260" y="137">0.30</text><text x="260" y="162">0.25</text><text x="260" y="186">0.20</text><text x="260" y="211">0.15</text><text x="260" y="235">0.10</text></g>
  <text class="h" x="301" y="86">Overall Scores <tspan font-weight="700" style="fill:var(--ink)">(0-1)</tspan></text>
  <g class="xs" text-anchor="middle"><text x="352" y="110">0</text><text x="434" y="110">0.25</text><text x="516" y="110">0.5</text><text x="598" y="110">0.75</text><text x="680" y="110">1</text></g>
  <g class="grid"><line x1="352" y1="116" x2="680" y2="116"/><line x1="680" y1="116" x2="680" y2="243"/></g>
  <line class="axis" x1="352" y1="116" x2="352" y2="243"/>
  <rect x="352" y="122" width="204" height="23" fill="var(--green)"/><rect x="352" y="153" width="256" height="23" fill="var(--teal)"/>
  <rect x="352" y="184" width="180" height="23" fill="var(--orange)"/><rect x="352" y="215" width="134" height="23" fill="var(--grey)"/>
  <g class="sm" font-weight="700" text-anchor="end"><text x="342" y="137">Option A</text><text x="342" y="168">Option B</text><text x="342" y="199">Option C</text><text x="342" y="230">Option D</text></g>
  <g class="val"><text x="561" y="137">0.6</text><text x="613" y="168">0.8</text><text x="537" y="199">0.6</text><text x="491" y="230">0.4</text></g>
  <rect x="39" y="255" width="659" height="64" rx="5" fill="#eeeeee"/>
  <rect x="48" y="263" width="94" height="48" rx="5" fill="var(--green-light)"/>
  <text x="95" y="283" font-size="13" font-weight="600" text-anchor="middle" style="fill:#fff">Ranked</text><text x="95" y="300" font-size="13" font-weight="600" text-anchor="middle" style="fill:#fff">Options</text>
  <g font-size="44" font-weight="700">
    <text x="164" y="306" style="fill:var(--teal)">1</text><text x="302" y="306" style="fill:var(--green)">2</text>
    <text x="432" y="306" style="fill:var(--orange)">3</text><text x="568" y="306" style="fill:var(--grey)">4</text>
  </g>
  <g class="lbl" font-weight="600"><text x="194" y="285">Option B</text><text x="331" y="285">Option A</text><text x="466" y="285">Option C</text><text x="601" y="285">Option D</text></g>
  <g class="xs"><text x="194" y="299">(0.78)</text><text x="331" y="299">(0.62)</text><text x="466" y="299">(0.55)</text><text x="601" y="299">(0.41)</text></g>
  <g stroke="#bbb"><line x1="268" y1="265" x2="268" y2="309"/><line x1="404" y1="265" x2="404" y2="309"/><line x1="539" y1="265" x2="539" y2="309"/></g>
  <rect x="40" y="336" width="658" height="56" rx="5" fill="var(--tint)"/><rect x="40" y="336" width="55" height="56" rx="5" fill="var(--green-dark)"/>
  <polygon points="67,348 71,359 83,360 74,367 77,379 67,372 57,379 60,367 51,360 63,359" fill="#fff"/>
  <text class="kf-h" x="106" y="358">KEY FINDING</text>
  <text class="kf-t" x="106" y="377">Option B is the preferred alternative considering all criteria and weights.</text>
</svg>
</section>

<!-- 06 Hydrogen, CCUS, PtX -->
<section class="slide col-l row4">
<svg viewBox="0 0 735 413" role="group" aria-label="Hydrogen, CCUS and Power-to-X">
  <rect x="37" y="17" width="32" height="30" fill="var(--green-dark)"/><text class="num" x="43" y="39">06</text>
  <text class="ttl" x="77" y="39">HYDROGEN, CCUS &amp; POWER-TO-X</text>
  <line x1="37" y1="58" x2="698" y2="58" stroke="var(--green-dark)" stroke-width="1.5"/>
  <text class="h" x="45" y="107">Power-to-X Pathway Efficiency (%)</text>
  <g class="xs" text-anchor="end"><text x="58" y="130">100</text><text x="58" y="158">80</text><text x="58" y="186">60</text><text x="58" y="214">40</text><text x="58" y="242">20</text><text x="58" y="269">0</text></g>
  <line class="axis" x1="64" y1="127" x2="64" y2="266"/><line class="axis" x1="64" y1="266" x2="345" y2="266"/>
  <rect x="75" y="126" width="40" height="140" fill="#2f8f3b"/>
  <rect x="130" y="126" width="40" height="21" fill="#b6d9b6"/><rect x="186" y="147" width="40" height="28" fill="#b6d9b6"/><rect x="242" y="175" width="40" height="14" fill="#b6d9b6"/>
  <rect x="298" y="189" width="40" height="77" fill="var(--teal)"/>
  <g class="sm" font-weight="700" text-anchor="middle"><text x="95" y="146" style="fill:#fff">100</text><text x="150" y="162">−15</text><text x="206" y="190">−20</text><text x="262" y="204">−10</text><text x="318" y="231" style="fill:#fff">55</text></g>
  <g class="xs" text-anchor="middle"><text x="95" y="278">Electricity</text><text x="95" y="288">(Input)</text><text x="150" y="278">Electrolysis</text><text x="206" y="278">Synthesis</text><text x="262" y="278">Upgrading &amp;</text><text x="262" y="288">Compression</text><text x="318" y="278">Product</text><text x="318" y="288">(Output)</text></g>
  <line x1="367" y1="95" x2="367" y2="300" stroke="#ddd"/>
  <text class="h" x="384" y="107">GHG Emissions <tspan class="hn">(kg CO₂-eq/kg product)</tspan></text>
  <g class="xs" text-anchor="end"><text x="394" y="130">8</text><text x="394" y="165">6</text><text x="394" y="199">4</text><text x="394" y="234">2</text><text x="394" y="269">0</text></g>
  <line class="axis" x1="400" y1="127" x2="400" y2="266"/><line class="axis" x1="400" y1="266" x2="700" y2="266"/>
  <rect x="420" y="150" width="50" height="116" fill="var(--grey)"/><rect x="511" y="230" width="50" height="36" fill="var(--teal)"/><rect x="604" y="257" width="50" height="9" fill="var(--green)"/>
  <g class="val" text-anchor="middle"><text x="445" y="145">6.7</text><text x="536" y="225">2.1</text><text x="629" y="252">0.5</text></g>
  <g class="xs" text-anchor="middle"><text x="445" y="278">Conventional</text><text x="445" y="288">(Reference)</text><text x="536" y="278">Conventional (Current</text><text x="536" y="288">Grid)</text><text x="629" y="278">Power-to-X (100% RES)</text></g>
  <rect x="40" y="336" width="658" height="56" rx="5" fill="var(--tint)"/><rect x="40" y="336" width="55" height="56" rx="5" fill="var(--green-dark)"/>
  <path d="M55 381c2-16 12-26 28-28c0 17-10 27-25 27zM57 379l17-17" fill="#fff" stroke="var(--green-dark)" stroke-width="1.5"/>
  <text class="kf-h" x="106" y="358">KEY FINDING</text>
  <text class="kf-t" x="106" y="377">Power-to-X with renewable electricity reduces GHG emissions by &gt;90% compared to conventional routes.</text>
</svg>
</section>

<!-- 07 Energy infrastructure -->
<section class="slide col-r row4">
<svg viewBox="0 0 735 413" role="group" aria-label="Energy infrastructure">
  <defs>
    <radialGradient id="gridMap" cx=".55" cy=".35" r=".7"><stop offset="0" stop-color="#2f9968"/><stop offset=".45" stop-color="#7cc49a"/><stop offset="1" stop-color="#dcefe3"/></radialGradient>
  </defs>
  <rect x="37" y="17" width="32" height="30" fill="var(--green-dark)"/><text class="num" x="43" y="39">07</text>
  <text class="ttl" x="77" y="39">ENERGY INFRASTRUCTURE</text>
  <line x1="37" y1="58" x2="698" y2="58" stroke="var(--green-dark)" stroke-width="1.5"/>
  <text class="h" x="39" y="86">GRID EXPANSION NEED (2023)</text>
  <text class="sm" x="39" y="100">Load increase vs. today (%)</text>
  <rect x="56" y="108" width="130" height="180" rx="14" fill="url(#gridMap)" role="img" aria-label="Regional map shaded by grid expansion need, highest in the central north"/>
  <g><rect x="42" y="292" width="30" height="6" fill="#dcefe3"/><rect x="77" y="292" width="30" height="6" fill="#b6dcc4"/><rect x="112" y="292" width="30" height="6" fill="#7cc49a"/><rect x="147" y="292" width="30" height="6" fill="#2f9968"/><rect x="182" y="292" width="30" height="6" fill="var(--green-dark)"/></g>
  <g class="xs" text-anchor="middle"><text x="57" y="311">&lt;10</text><text x="92" y="311">10–25</text><text x="127" y="311">25–50</text><text x="162" y="311">50–75</text><text x="197" y="311">&gt;75%</text></g>
  <line x1="223" y1="80" x2="223" y2="320" stroke="#ddd"/><line x1="451" y1="80" x2="451" y2="320" stroke="#ddd"/>
  <text class="h" x="242" y="86">GENERATION MIX (2035)</text>
  <g transform="rotate(-90 360 178)" fill="none" stroke-width="32">
    <circle cx="360" cy="178" r="51" stroke="var(--green)" stroke-dasharray="108.9 320.4"/>
    <circle cx="360" cy="178" r="51" stroke="var(--orange)" stroke-dasharray="89.7 320.4" stroke-dashoffset="-108.9"/>
    <circle cx="360" cy="178" r="51" stroke="var(--teal)" stroke-dasharray="57.7 320.4" stroke-dashoffset="-198.6"/>
    <circle cx="360" cy="178" r="51" stroke="#3a3a3a" stroke-dasharray="32 320.4" stroke-dashoffset="-256.3"/>
    <circle cx="360" cy="178" r="51" stroke="#a6a8aa" stroke-dasharray="32.1 320.4" stroke-dashoffset="-288.3"/>
  </g>
  <g class="xs" font-weight="700" text-anchor="middle"><text x="410" y="161" style="fill:#fff">34%</text><text x="372" y="241" style="fill:#fff">28%</text><text x="317" y="198" style="fill:#fff">18%</text><text x="320" y="153" style="fill:#fff">10%</text><text x="350" y="135" style="fill:#fff">10%</text></g>
  <g class="sm">
    <circle cx="286" cy="285" r="3.5" fill="var(--green)"/><text x="295" y="288">Wind</text>
    <circle cx="346" cy="285" r="3.5" fill="var(--teal)"/><text x="355" y="288">Hydro</text>
    <circle cx="405" cy="285" r="3.5" fill="#a6cf7e"/><text x="414" y="288">Biomass</text>
    <circle cx="286" cy="304" r="3.5" fill="var(--orange)"/><text x="295" y="307">Solar</text>
    <circle cx="346" cy="304" r="3.5" fill="#3a3a3a"/><text x="355" y="307">Gas</text>
    <circle cx="405" cy="304" r="3.5" fill="#a6a8aa"/><text x="414" y="307">Other</text>
  </g>
  <text class="h" x="501" y="86">STORAGE UTILIZATION</text>
  <text class="sm" x="501" y="100">(Full Load Hours)</text>
  <g class="sm" text-anchor="end"><text x="535" y="126">8000</text><text x="535" y="164">6000</text><text x="535" y="202">4000</text><text x="535" y="240">2000</text><text x="535" y="278">0</text></g>
  <g class="grid"><line x1="543" y1="122" x2="700" y2="122"/><line x1="543" y1="160" x2="700" y2="160"/><line x1="543" y1="198" x2="700" y2="198"/><line x1="543" y1="236" x2="700" y2="236"/><line x1="543" y1="274" x2="700" y2="274"/></g>
  <g stroke="#555" stroke-width="1">
    <path d="M551 213v52M546 213h10M546 265h10"/><rect x="540" y="225" width="21" height="24" fill="var(--green-light)"/><path d="M540 239h21"/>
    <path d="M590 167v64M585 167h10M585 231h10"/><rect x="580" y="178" width="21" height="31" fill="var(--teal)"/><path d="M580 191h21"/>
    <path d="M633 163v72M628 163h10M628 235h10"/><rect x="622" y="192" width="21" height="33" fill="var(--orange)"/><path d="M622 212h21"/>
    <path d="M675 149v86M670 149h10M670 235h10"/><rect x="664" y="170" width="22" height="40" fill="#f07a3a"/><path d="M664 188h22"/>
  </g>
  <g class="sm" text-anchor="middle" style="fill:var(--muted)"><text x="551" y="308">Battery</text><text x="590" y="308">P2G</text><text x="633" y="308">Thermal</text><text x="675" y="308">Hydro</text></g>
  <rect x="40" y="336" width="658" height="56" rx="5" fill="var(--tint)"/><rect x="40" y="336" width="55" height="56" rx="5" fill="var(--green-dark)"/>
  <g fill="#fff"><rect x="61" y="344" width="3" height="8"/><rect x="70" y="344" width="3" height="8"/><path d="M56 352h22v10c0 6-5 10-11 10s-11-4-11-10z"/><rect x="65" y="372" width="4" height="10"/></g>
  <path d="M68 355l-4 7h5l-3 7" fill="none" stroke="var(--green-dark)" stroke-width="1.5"/>
  <text class="kf-h" x="106" y="352">KEY FINDING</text>
  <text class="kf-t" x="106" y="369">High shares of wind and solar require storage and grid expansion, with P2G and hydro providing</text>
  <text class="kf-t" x="106" y="383">seasonal flexibility.</text>
</svg>
</section>

<!-- 08 Industrial processes & circular economy -->
<section class="slide col-l row5">
<svg viewBox="0 0 735 413" role="group" aria-label="Industrial processes and circular economy">
  <defs><pattern id="hatch" width="4" height="4" patternUnits="userSpaceOnUse"><rect width="4" height="4" fill="#e6e6e6"/><path d="M0 4L4 0" stroke="#bbb" stroke-width="0.8"/></pattern></defs>
  <rect x="37" y="17" width="32" height="30" fill="var(--green-dark)"/><text class="num" x="43" y="39">08</text>
  <text class="ttl" x="77" y="39">INDUSTRIAL PROCESSES &amp; CIRCULAR ECONOMY</text>
  <line x1="37" y1="58" x2="698" y2="58" stroke="var(--green-dark)" stroke-width="1.5"/>
  <text class="h" x="39" y="97">Material Circularity Indicator (MCI)</text>
  <g class="sm" text-anchor="end"><text x="52" y="129">1.5</text><text x="52" y="172">1.0</text><text x="52" y="215">0.5</text><text x="52" y="257">0.0</text></g>
  <line class="axis" x1="60" y1="125" x2="60" y2="254"/><line class="axis" x1="60" y1="254" x2="345" y2="254"/>
  <rect x="75" y="230" width="40" height="24" fill="var(--green)"/><rect x="139" y="215" width="40" height="39" fill="var(--teal)"/>
  <rect x="202" y="192" width="40" height="62" fill="var(--orange)"/><rect x="288" y="177" width="40" height="77" fill="url(#hatch)" stroke="#777" stroke-dasharray="3 2"/>
  <g class="val" text-anchor="middle"><text x="95" y="224">0.28</text><text x="159" y="209">0.46</text><text x="222" y="186">0.72</text><text x="308" y="171">0.90</text></g>
  <g class="sm" text-anchor="middle"><text x="95" y="271">Product A</text><text x="159" y="271">Product B</text><text x="222" y="271">Product C</text><text x="308" y="271">Target</text><text x="308" y="283">(2030)</text></g>
  <line x1="367" y1="85" x2="367" y2="300" stroke="#ddd"/>
  <text class="h" x="393" y="97">Environmental Impact <tspan class="hn">(per functional unit)</tspan></text>
  <g class="sm" text-anchor="end"><text x="409" y="129">1.2</text><text x="409" y="172">0.8</text><text x="409" y="215">0.4</text><text x="409" y="257">0.0</text></g>
  <line class="axis" x1="416" y1="125" x2="416" y2="254"/><line class="axis" x1="416" y1="254" x2="590" y2="254"/>
  <rect x="437" y="203" width="43" height="51" fill="var(--teal)"/><rect x="437" y="169" width="43" height="34" fill="var(--grey-light)"/><rect x="437" y="146" width="43" height="23" fill="var(--green)"/>
  <rect x="513" y="246" width="43" height="8" fill="var(--teal)"/><rect x="513" y="224" width="43" height="22" fill="var(--green)"/><rect x="513" y="202" width="43" height="22" fill="var(--teal)"/>
  <text class="val" x="458" y="140" text-anchor="middle">1.00</text><text class="val" x="534" y="217" text-anchor="middle" style="fill:#fff">0.48</text>
  <g class="sm" text-anchor="middle"><text x="458" y="271">Current</text><text x="458" y="283">(linear)</text><text x="534" y="271">Circular</text><text x="534" y="283">(improved)</text></g>
  <g class="sm">
    <rect x="611" y="120" width="9" height="9" fill="var(--green)"/><text x="626" y="128">Raw Material</text>
    <rect x="611" y="142" width="9" height="9" fill="var(--teal)"/><text x="626" y="150">Production</text>
    <rect x="611" y="164" width="9" height="9" fill="var(--grey-light)"/><text x="626" y="172">Transport</text>
    <rect x="611" y="186" width="9" height="9" fill="var(--orange)"/><text x="626" y="194">Use Phase</text>
    <rect x="611" y="208" width="9" height="9" fill="var(--green-dark)"/><text x="626" y="216">End-of-life</text>
  </g>
  <rect x="40" y="336" width="658" height="56" rx="5" fill="var(--tint)"/><rect x="40" y="336" width="55" height="56" rx="5" fill="var(--green-dark)"/>
  <circle cx="67" cy="364" r="13" fill="none" stroke="#fff" stroke-width="3.5" stroke-dasharray="22 5"/>
  <text class="kf-h" x="106" y="358">KEY FINDING</text>
  <text class="kf-t" x="106" y="377">Circular strategies significantly increase material circularity and reduce environmental impacts.</text>
</svg>
</section>

<!-- 09 GIS-based site analysis -->
<section class="slide col-r row5">
<svg viewBox="0 0 735 413" role="group" aria-label="GIS-based site and potential analysis">
  <defs>
    <linearGradient id="solarMap" x1="0" y1="0" x2=".3" y2="1"><stop offset="0" stop-color="#fbe7a6"/><stop offset=".35" stop-color="#f8c94f"/><stop offset=".65" stop-color="#f29b1c"/><stop offset="1" stop-color="#e0531c"/></linearGradient>
    <linearGradient id="suitMap" x1="0" y1="0" x2=".3" y2="1"><stop offset="0" stop-color="#d9ecb8"/><stop offset=".4" stop-color="#7cc553"/><stop offset=".7" stop-color="#45b06c"/><stop offset="1" stop-color="#17706e"/></linearGradient>
    <linearGradient id="siteMap" x1="0" y1="0" x2=".3" y2="1"><stop offset="0" stop-color="#d3d5d3"/><stop offset=".45" stop-color="#d7e9bf"/><stop offset=".8" stop-color="#a6d7b0"/><stop offset="1" stop-color="#6cc3b0"/></linearGradient>
  </defs>
  <rect x="37" y="17" width="32" height="30" fill="var(--green-dark)"/><text class="num" x="43" y="39">09</text>
  <text class="ttl" x="77" y="39">GIS-BASED SITE &amp; POTENTIAL ANALYSIS</text>
  <line x1="37" y1="58" x2="698" y2="58" stroke="var(--green-dark)" stroke-width="1.5"/>
  <text class="h" x="128" y="86" text-anchor="middle">Solar PV Annual Yield</text>
  <text class="sm" x="128" y="99" text-anchor="middle">(GHI, kWh/m²-a)</text>
  <rect x="56" y="106" width="136" height="148" rx="14" fill="url(#solarMap)" role="img" aria-label="Regional map of annual solar yield, rising from north to south"/>
  <g class="sm">
    <rect x="40" y="259" width="9" height="9" fill="#fbe39a"/><text x="55" y="267">&lt; 1,000</text>
    <rect x="40" y="271" width="9" height="9" fill="#f8c94f"/><text x="55" y="279">1,000 – 1,200</text>
    <rect x="40" y="283" width="9" height="9" fill="#f5a623"/><text x="55" y="291">1,200 – 1,400</text>
    <rect x="40" y="295" width="9" height="9" fill="#ef7d22"/><text x="55" y="303">1,400 – 1,600</text>
    <rect x="40" y="307" width="9" height="9" fill="#d9401a"/><text x="55" y="315">&gt; 1,600</text>
  </g>
  <line x1="223" y1="80" x2="223" y2="320" stroke="#ddd"/><line x1="451" y1="80" x2="451" y2="320" stroke="#ddd"/>
  <text class="h" x="337" y="86" text-anchor="middle">Suitability Map</text>
  <text class="sm" x="337" y="99" text-anchor="middle">(Weighted Score 0–1)</text>
  <rect x="272" y="106" width="136" height="148" rx="14" fill="url(#suitMap)" role="img" aria-label="Regional map of weighted site suitability, highest in the south"/>
  <g class="sm">
    <rect x="259" y="259" width="9" height="9" fill="#e3f0c8"/><text x="274" y="267">0 – 0.2</text>
    <rect x="259" y="271" width="9" height="9" fill="#b5dc8a"/><text x="274" y="279">0.2 – 0.4</text>
    <rect x="259" y="283" width="9" height="9" fill="#6cbf4a"/><text x="274" y="291">0.4 – 0.6</text>
    <rect x="259" y="295" width="9" height="9" fill="#2f9a6a"/><text x="274" y="303">0.6 – 0.8</text>
    <rect x="259" y="307" width="9" height="9" fill="#17706e"/><text x="274" y="315">0.8 – 1.0</text>
  </g>
  <text class="h" x="547" y="86" text-anchor="middle">Top Candidate Sites</text>
  <rect x="480" y="100" width="136" height="196" rx="14" fill="url(#siteMap)" role="img" aria-label="Regional map with three candidate sites marked"/>
  <g font-size="10" font-weight="700">
    <circle cx="553" cy="143" r="8" fill="var(--green-dark)"/><text x="553" y="147" text-anchor="middle" style="fill:#fff">1</text>
    <circle cx="543" cy="194" r="8" fill="var(--green-dark)"/><text x="543" y="198" text-anchor="middle" style="fill:#fff">2</text>
    <circle cx="592" cy="256" r="8" fill="var(--green-dark)"/><text x="592" y="260" text-anchor="middle" style="fill:#fff">3</text>
  </g>
  <rect x="478" y="305" width="9" height="9" fill="var(--green-light)"/><text class="sm" x="493" y="313">High suitability area</text>
  <rect x="40" y="336" width="658" height="56" rx="5" fill="var(--tint)"/><rect x="40" y="336" width="55" height="56" rx="5" fill="var(--green-dark)"/>
  <path d="M67 384c-9-11-14-18-14-25a14 14 0 0 1 28 0c0 7-5 14-14 25z" fill="#fff"/><circle cx="67" cy="359" r="5" fill="var(--green-dark)"/>
  <text class="kf-h" x="106" y="358">KEY FINDING</text>
  <text class="kf-t" x="106" y="377">Several high-potential zones are identified along main roads and nearby grid sites.</text>
</svg>
</section>

</body>
</html>
```